Business Card Design - Law Firm

We are a boutique law firm located near the beach in Manly, Australia. We have recently had a new logo designed and are revamping our business cards with the new logo.

We have recently had a business card design done for us but are not entirely happy with it. We are looking for something modern, simplistic but striking. We would like to see multiple designs.

We have attached a word document which includes our new logo and the current business card design which we are looking at moving away from.

We would like the business cards to be double sided. We would like the design to include something which we can print in gloss colour when we send it to the business card printers.

```html
<!DOCTYPE html>
<html lang="en">
<head>
<meta charset="utf-8">
<title>Harcourt &amp; Partners Lawyers – Business Card</title>
<link rel="stylesheet" href="https://fonts.googleapis.com/css2?family=Montserrat:wght@400;600;700&display=swap">
<style>
  :root {
    --stage: #e6e6e8;
    --card-black: #161616;
    --card-black-soft: #222;
    --paper: #ffffff;
    --navy: #2f3a85;
    --gold: #c4ad6e;
    --periwinkle: #6f82c9;
    --ink: #1a1a1a;
    --white: #ffffff;
  }
  * { margin: 0; padding: 0; box-sizing: border-box; }
  html, body { width: 1200px; height: 1200px; overflow: hidden; }
  body {
    background: var(--stage);
    font-family: "Montserrat", sans-serif;
    display: flex;
    flex-direction: column;
    align-items: center;
    justify-content: center;
    gap: 60px;
  }
  .card {
    position: relative;
    width: 860px;
    height: 491px;
    border-radius: 26px;
    overflow: hidden;
    box-shadow: 0 6px 18px rgba(0,0,0,0.18);
  }

  /* Front */
  .card--front { background: var(--card-black); }
  .front-texture {
    position: absolute; inset: 0;
    background: radial-gradient(ellipse at 50% 45%, var(--card-black-soft) 0%, var(--card-black) 70%);
  }
  .front-brand {
    position: absolute; inset: 0;
    display: flex; align-items: center; justify-content: center; gap: 18px;
  }
  .brand-dot {
    width: 26px; height: 26px; border-radius: 50%;
    background: var(--periwinkle);
  }
  .brand-name {
    font-weight: 600;
    font-size: 36px;
    letter-spacing: 0.06em;
    color: var(--white);
  }

  /* Back */
  .card--back { background: var(--paper); }
  .back-wave { position: absolute; inset: 0; }
  .back-brand {
    position: absolute; left: 120px; top: 150px;
    display: flex; align-items: center; gap: 16px;
  }
  .back-brand .brand-dot { background: var(--navy); width: 22px; height: 22px; }
  .back-brand .brand-name { color: var(--ink); font-size: 30px; }

  .holder {
    position: absolute; left: 100px; bottom: 34px;
    color: var(--white);
  }
  .holder-name { font-weight: 700; font-size: 30px; letter-spacing: 0.01em; line-height: 1.2; }
  .holder-role { font-weight: 400; font-size: 18px; margin-top: 2px; }

  .contact {
    position: absolute; left: 500px; top: 312px;
    color: var(--white); font-size: 16px; line-height: 1.45;
    list-style: none;
  }
  .contact-address { font-weight: 600; margin-bottom: 6px; }
  .contact li { display: flex; align-items: center; gap: 9px; font-weight: 600; }
  .contact svg { width: 15px; height: 15px; flex: none; }
</style>
</head>
<body>

  <section class="card card--front" aria-label="Card front">
    <div class="front-texture" role="img" aria-label="Faint dotted world map texture on black"></div>
    <div class="front-brand">
      <span class="brand-dot"></span>
      <span class="brand-name">Harcourt &amp; Partners Lawyers</span>
    </div>
  </section>

  <section class="card card--back" aria-label="Card back">
    <svg class="back-wave" viewBox="0 0 860 491" aria-hidden="true">
      <path fill="var(--navy)" d="M0,420 C250,330 520,300 640,280 C740,262 810,230 860,195 L860,491 L0,491 Z"/>
      <path fill="none" stroke="var(--gold)" stroke-width="10" d="M-5,406 C250,314 520,284 640,264 C740,246 810,214 865,176"/>
    </svg>

    <div class="back-brand">
      <span class="brand-dot"></span>
      <span class="brand-name">Harcourt &amp; Partners Lawyers</span>
    </div>

    <div class="holder">
      <p class="holder-name">MARA LINDQVIST</p>
      <p class="holder-role">Practice Manager</p>
    </div>

    <ul class="contact">
      <li class="contact-address">Suite 4, 12 Pier Lane<br>COVEDALE NSW 2190</li>
      <li>
        <svg viewBox="0 0 16 16"><path fill="#fff" d="M3.5 1.5l2.5 0 1 3.5-1.6 1.2c.8 1.7 2 2.9 3.7 3.7L10.3 8.3l3.5 1v2.5c0 1-1 1.8-2 1.7C6.3 13 2.9 9.7 2 4c-.1-1 .6-2.5 1.5-2.5z"/></svg>
        (02) 5550 1847
      </li>
      <li>
        <svg viewBox="0 0 16 16"><rect x="1.5" y="3.5" width="13" height="9" rx="1" fill="none" stroke="#fff" stroke-width="1.5"/><path d="M2 4l6 5 6-5" fill="none" stroke="#fff" stroke-width="1.5"/></svg>
        mara.lindqvist@covedalelaw.com.au
      </li>
      <li>
        <svg viewBox="0 0 16 16"><circle cx="8" cy="8" r="6.3" fill="none" stroke="#fff" stroke-width="1.4"/><ellipse cx="8" cy="8" rx="2.8" ry="6.3" fill="none" stroke="#fff" stroke-width="1.2"/><path d="M1.7 8h12.6" stroke="#fff" stroke-width="1.2"/></svg>
        www.harcourtandpartners.com.au
      </li>
    </ul>
  </section>

</body>
</html>
```